Landing Page Side by Side With Dr. Korwell

Hello!

I am looking for a high converting Landing Page for a One on One Coaching program that Dr. Korwell is releasing. I created a moch up for content but the spacing and graphics are not cohesive. I like the medical look at the top of the first page - the image is the graphic "Get Side BY Side Support from Dr. Korwell.
Please let me know if you have any questions!
Thank you!

```html
<!DOCTYPE html>
<html lang="en">
<head>
<meta charset="utf-8">
<title>Side by Side With Dr. Korwell</title>
<link rel="stylesheet" href="https://fonts.googleapis.com/css2?family=Bebas+Neue&family=Open+Sans:wght@400;600;700&display=swap">
<style>
  :root{
    --navy:#142d8a;
    --footer:#0f1f5c;
    --maroon:#6b1640;
    --ink:#1d1d1d;
    --muted:#555;
    --white:#fff;
    --line:#bdbdbd;
  }
  *{box-sizing:border-box;margin:0;padding:0}
  html,body{width:762px;height:1200px;overflow:hidden;background:var(--white)}
  body{position:relative;font-family:"Open Sans",sans-serif;color:var(--ink)}
  .abs{position:absolute}
  .display{font-family:"Bebas Neue",sans-serif;letter-spacing:-.5px;line-height:1}

  /* header */
  .site-header{left:0;top:0;width:762px;height:52px;background:var(--white)}
  .brand{left:84px;top:12px;display:flex;align-items:center;gap:6px;font-size:30px;color:var(--navy)}
  .brand-dot{width:12px;height:12px;border-radius:50%;background:var(--maroon)}
  .main-nav{right:84px;top:21px;display:flex;gap:17px;font-family:"Bebas Neue",sans-serif;font-size:13px;color:#444;letter-spacing:.2px}
  .main-nav .active{color:var(--navy)}

  /* hero */
  .hero{left:0;top:52px;width:762px;height:338px;overflow:hidden}
  .hero-photo{position:absolute;inset:0;background:linear-gradient(90deg,#e9eef1 0%,#dfe7ea 40%,#cfdde2 70%,#bcd0d6 100%)}
  .hero-doctor{position:absolute;left:0;top:20px;width:248px;height:318px;background:linear-gradient(180deg,#d9d3cf 0%,#f3f3f3 40%,#ffffff 100%)}
  .hero-heart{position:absolute;left:218px;top:30px;width:240px;height:290px;background:radial-gradient(ellipse at center,rgba(150,110,140,.35) 0%,rgba(150,110,140,0) 70%)}
  .hero-title{position:absolute;right:84px;top:80px;text-align:right;font-size:38px;color:var(--maroon)}
  .hero-sub{position:absolute;right:84px;top:159px;font-size:16px;color:#111}
  .hero-arrow{position:absolute;top:162px}

  /* intro */
  .intro-title{left:0;width:762px;top:438px;text-align:center;font-size:27px;color:var(--navy)}
  .intro-text{left:86px;width:592px;top:468px;text-align:center;font-size:9.6px;line-height:15px}
  .commit-title{left:0;width:762px;top:511px;text-align:center;font-size:14px;font-weight:700;letter-spacing:.3px}
  .goal{font-size:11px;display:flex;align-items:center;gap:8px;white-space:nowrap}
  .goal svg{width:11px;height:11px;fill:#333}

  /* coaching band */
  .coaching{left:0;top:657px;width:762px;height:325px;overflow:hidden}
  .coaching-photo{position:absolute;inset:0;background:radial-gradient(ellipse at 50% 40%,#a69a8f 0%,#6f6a63 45%,#4c4f4a 100%)}
  .coaching-title{position:absolute;left:0;width:762px;top:47px;text-align:center;font-size:25px;color:var(--white)}
  .coaching-sub{position:absolute;left:0;width:762px;top:76px;text-align:center;font-size:15px;font-weight:600;color:var(--white)}
  .coaching-lead{position:absolute;left:0;width:762px;top:99px;text-align:center;font-size:9px;color:#eee}
  .pillar{position:absolute;top:131px;width:105px;height:149px;background:var(--white);text-align:center;padding:11px 8px 0}
  .pillar svg{width:34px;height:34px;fill:none;stroke:#222;stroke-width:1.6}
  .pillar h3{font-size:9px;font-weight:700;margin:4px 0 5px}
  .pillar p{font-size:5.6px;line-height:9px;color:var(--muted)}

  /* signup */
  .signup-title{left:0;width:762px;top:1030px;text-align:center;font-size:27px;color:var(--navy)}
  .field{top:1062px;height:27px;border:1px solid var(--line);font-size:8px;color:#666;padding:0 9px;line-height:25px}
  .subscribe{left:535px;top:1062px;width:67px;height:27px;background:var(--navy);color:var(--white);font-family:"Bebas Neue",sans-serif;font-size:14px;text-align:center;line-height:28px}

  /* footer */
  .site-footer{left:0;top:1139px;width:762px;height:61px;background:var(--footer);color:#c7cde2;font-size:7px}
  .footer-links{position:absolute;left:85px;top:17px;word-spacing:1px}
  .copyright{position:absolute;left:85px;top:34px}
  .social{position:absolute;top:25px;width:9px;height:9px;border-radius:50%;background:#c7cde2}
</style>
</head>
<body>

<header class="site-header abs">
  <div class="brand abs display">DR.KORWELL<span class="brand-dot"></span></div>
  <nav class="main-nav abs">
    <span class="active">HOME</span><span>ABOUT US</span><span>SERVICES</span><span>REVIEWS</span><span>CONTACT US</span>
  </nav>
</header>

<section class="hero abs">
  <div class="hero-photo" role="img" aria-label="Blurred bright clinic interior with staff"></div>
  <div class="hero-doctor" role="img" aria-label="Smiling doctor in white coat with arms crossed"></div>
  <div class="hero-heart" role="img" aria-label="Faint heart shape formed by two figures"></div>
  <h1 class="hero-title display">GET SIDE BY SIDE SUPPORT<br>FROM DR. KORWELL</h1>
  <p class="hero-sub">Total Wellness Coaching Program</p>
  <svg class="hero-arrow" style="left:30px" width="14" height="20" viewBox="0 0 14 20"><path d="M11 2 3 10l8 8" fill="none" stroke="#111" stroke-width="3"/></svg>
  <svg class="hero-arrow" style="left:718px" width="14" height="20" viewBox="0 0 14 20"><path d="m3 2 8 8-8 8" fill="none" stroke="#111" stroke-width="3"/></svg>
</section>

<h2 class="intro-title abs display">CONCIERGE TOTAL WELLNESS FROM A PRACTICING MD!</h2>
<p class="intro-text abs">Why wait for a doctors appointment when you can receive one on one care on an ongoing basis. Dr. Korwell currently has a four-month wait list to see him in his practice.</p>
<h3 class="commit-title abs">MAKE A COMMITMENT TO YOURSELF</h3>

<div class="goal abs" style="left:86px;top:541px"><svg viewBox="0 0 10 10"><circle cx="5" cy="5" r="5"/></svg>Lose Weight</div>
<div class="goal abs" style="left:86px;top:567px"><svg viewBox="0 0 10 10"><circle cx="5" cy="5" r="5"/></svg>Conquer Mental Illness</div>
<div class="goal abs" style="left:86px;top:592px"><svg viewBox="0 0 10 10"><circle cx="2.5" cy="4" r="2"/><circle cx="7.5" cy="4" r="2"/><rect x="0" y="6.5" width="10" height="3.5" rx="1.5"/></svg>Build A Better Tribe</div>
<div class="goal abs" style="left:321px;top:541px"><svg viewBox="0 0 10 10"><path d="M0 5h10M5 1l3 4-3 4"/><rect x="0" y="4" width="10" height="2"/></svg>Combat Stress R. Disease</div>
<div class="goal abs" style="left:321px;top:567px"><svg viewBox="0 0 10 10"><path d="M5 0C7 3 9 5 9 7a4 3 0 0 1-8 0C1 5 3 3 5 0z"/></svg>Increase Energy</div>
<div class="goal abs" style="left:321px;top:592px"><svg viewBox="0 0 10 10"><circle cx="5" cy="1.5" r="1.5"/><rect x="3.5" y="3.5" width="3" height="6.5"/></svg>Live Joyfully</div>
<div class="goal abs" style="left:554px;top:541px"><svg viewBox="0 0 10 10"><path d="M5 9 1 5a2.3 2.3 0 0 1 4-3 2.3 2.3 0 0 1 4 3z"/></svg>Cultivate Relationships</div>
<div class="goal abs" style="left:554px;top:567px"><svg viewBox="0 0 10 10"><circle cx="7" cy="3" r="3"/><path d="M5 5 0 10" stroke="#333" stroke-width="2"/></svg>Clarify Your Purpose</div>

<section class="coaching abs">
  <div class="coaching-photo" role="img" aria-label="Smiling woman relaxing indoors, darkened backdrop"></div>
  <h2 class="coaching-title display">SIGN ME UP FOR SIDE BY SIDE COACHING WITH DR. KORWELL</h2>
  <p class="coaching-sub">Still on the fence?&nbsp; Learn More</p>
  <p class="coaching-lead">Dr. Korwell Coaches You Side by Side in areas based on his Five Pillar Formula for Total Wellness :</p>

  <article class="pillar" style="left:84px">
    <svg viewBox="0 0 34 34"><rect x="4" y="12" width="7" height="18" rx="2"/><path d="M7 4v8"/><ellipse cx="20" cy="24" rx="9" ry="6"/><path d="M16 16l4-6 4 6"/></svg>
    <h3>NUTRITION</h3>
    <p>Fuel your body in the right ways. With the latest tools and research findings about nutrition, you'll learn how to change your body on a cellular level for a longer life and true vitality.</p>
  </article>
  <article class="pillar" style="left:206px">
    <svg viewBox="0 0 34 34"><circle cx="22" cy="5" r="3"/><path d="M11 13l7-3 5 5 6 1M18 10l-4 10 6 4-3 8M14 20l-5 7H3"/></svg>
    <h3>MOVEMENT</h3>
    <p>Combat daily stressors and degenerative disease through the implementation of exercise. Learn about the principles of movement and find out how to increase motility and vitality at any age.</p>
  </article>
  <article class="pillar" style="left:328px">
    <svg viewBox="0 0 34 34"><path d="M17 32V16M17 16C10 18 3 14 3 6c8 0 14 3 14 10zM17 16c4-6 10-9 14-9 0 7-6 10-14 9"/></svg>
    <h3>TRIBE</h3>
    <p>Gain perspective and information on the unique healing powers of having a tribe. Learn about practices that will assist you in becoming more conscious of who is in your tribe how they affect your everyday health.</p>
  </article>
  <article class="pillar" style="left:450px">
    <svg viewBox="0 0 34 34"><path d="M17 4c-4-2-10 0-10 5-4 2-4 8 0 10-1 5 4 9 10 8zM17 4c4-2 10 0 10 5 4 2 4 8 0 10 1 5-4 9-10 8zM17 4v23"/></svg>
    <h3>MINDFULNESS</h3>
    <p>Take a deep dive into individual mindfulness practices that will help you reduce stress, overcome anxiety, conquer disease, and increase your overall wellbeing through methods of peaceful living.</p>
  </article>
  <article class="pillar" style="left:573px">
    <svg viewBox="0 0 34 34"><circle cx="16" cy="18" r="13"/><circle cx="16" cy="18" r="8"/><circle cx="16" cy="18" r="3"/><path d="M16 18 29 5M25 5h4v4"/></svg>
    <h3>PURPOSE</h3>
    <p>Find out how clarifying your purpose can bring about powerful health benefits that will improve your life. Learn and develop skills to find and attain your purpose through foolproof</p>
  </article>
</section>

<h2 class="signup-title abs display">SIGN ME UP! I AM READY FOR CHANGE</h2>
<div class="field abs" style="left:159px;width:179px">Name</div>
<div class="field abs" style="left:347px;width:179px">Email Address</div>
<div class="subscribe abs">SUBSCRIBE</div>

<footer class="site-footer abs">
  <p class="footer-links">Home &nbsp;|&nbsp; About Us &nbsp;|&nbsp; Services &nbsp;|&nbsp; Reviews &nbsp;|&nbsp; Contact Us</p>
  <p class="copyright">Copyright &copy; 2018 Dr. Korwell.&nbsp;&nbsp; All rights reserved.</p>
  <span class="social" style="left:646px"></span>
  <span class="social" style="left:668px"></span>
</footer>

</body>
</html>
```